Kea Ridge Charts needs some standard web ads

Kea Ridge Charts needs banner ads designed in VARIOUS SIZES. Can be static (PNG, GIF, JPG) or animated GIF. Maximum file size for each ad is 50 KB (for use with Plexa PromoLine).

These are just for general promotion of the free online topo map service Kea Ridge Charts. I'm open to text suggestions, but here's some ideas that might work well:

Main text: "Free online topo map"
Secondary text (if required): "Using the official VOMR topo maps"
Secondary text / button text (if required): "Go explore" / "Explore" / etc.

Text capitalisation: Whatever looks / reads best.

The banners should be catchy and interesting while obviously enticing the user to click. Background on our site can be found on the info tab at: http://www.kearidgecharts.co.nz

For initial design selection to save time only 3 banner sizes are required:

728 x 90 (Leaderboard)
160 x 600 (Wide Skyscraper)
300 x 250 (Medium Rectangle)

But for the final product I'd like the following sizes:

728 x 90 (Leaderboard)
468 x 60 (Banner)
120 x 600 (Skyscraper)
200 x 200 (Small Square)
250 x 250 (Square)
336 x 280 (Large Rectangle)
Updates

The brief has been updated to include some ideas about potential text for the ads:

These are just for general promotion of the free online topo map service Kea Ridge Charts. I'm open to text suggestions, but here's some that might work well:

Secondary text / button text (if required): "Go explore" / "Plan an adventure" / etc.

Reason: Sorry for the lack of feedback recently. Been a little too busy with Christmas approaching and a few issues with ISP. I pretty much have a design picked out now - just working with the designer to get some minor tweaks, so please don't submit anymore designs unless asked as I'd hate for anyone to waste their time. Thank you everyone for your effort.s It's been a hard decision to make regarding the design to go for! Cheers, Trent

Target Market(s)

The site is mainly used by outdoorsy people interested in tramping (hiking), climbing, hunting, geo-caching, etc.

Industry/Entity Type

Plexa

Requirements
Must have
• Kea Ridge Charts logo, or at least the pin logo element.

Topo (Relief40) map showing - I'd ideally like to see this as the major graphic element, presented well. Simple designs are fine!
TIFF map images available here:
ftp://relief.vomr.example.nz/Relief40_raster_images/GeoTIFFRelief40/

Please use New Zealand (British) spelling.

For access to TIFF Relief40 maps images for use in the design:
Open the downloads tab at the top of www.kearidgecharts.co.nz and click on any of the rectangles that appear over the map to download the relevant GeoTIFF map you'd like to use (GeoTIFF is just a TIFF with some extra meta data attached, so it just like a normal TIFF for designers).
Should not have
• Photos. I'm more interested in seeing a nice sliver of topo map presented well.

```html
<!DOCTYPE html>
<html lang="en-NZ">
<head>
<meta charset="utf-8">
<title>Kea Ridge Charts – Web Banner Set</title>
<link rel="stylesheet" href="https://fonts.googleapis.com/css2?family=Arvo:wght@700&family=Open+Sans:wght@400;600;700&display=swap">
<style>
  :root {
    --stage: #6e4b33;
    --panel-dark: #181818;
    --lime: #8dbb2f;
    --lime-bright: #a6d03a;
    --lime-text: #9ccb34;
    --text-white: #ffffff;
    --text-grey: #c9c9c9;
    --sub-dark: #1d2a06;
    --map-mint: #dce9c6;
    --map-green: #c4dba6;
    --map-cream: #eef1d9;
    --map-orange: #ecc98f;
    --map-blue: #bcd9d8;
    --btn-top: #ffd04a;
    --btn-bottom: #f39a12;
    --btn-text: #5a2d00;
    --frame: #f2f2f2;
  }
  * { box-sizing: border-box; margin: 0; padding: 0; }
  html, body { width: 1200px; height: 758px; overflow: hidden; }
  body {
    background: var(--stage);
    font-family: "Open Sans", Arial, sans-serif;
    position: relative;
  }
  .banner {
    position: absolute;
    overflow: hidden;
    border: 1px solid var(--frame);
    box-shadow: 0 3px 8px rgba(0,0,0,.45);
  }
  .map-fill {
    position: absolute;
    inset: 0;
    background: linear-gradient(160deg, var(--map-cream) 0%, var(--map-mint) 30%, var(--map-green) 55%, var(--map-mint) 75%, var(--map-orange) 100%);
  }
  .map-fill.coastal {
    background: linear-gradient(100deg, var(--map-mint) 0%, var(--map-green) 45%, var(--map-orange) 70%, var(--map-blue) 100%);
  }

  /* Brand header (tall and box formats) */
  .brand-head {
    position: absolute;
    left: 0; top: 0; width: 100%;
    background: var(--panel-dark);
  }
  .brand-curve {
    position: absolute;
    left: 0; width: 100%;
    display: block;
  }
  .brand-mark {
    display: block;
    border-radius: 50%;
    background: var(--lime);
  }
  .brand-name {
    font-weight: 600;
    color: var(--text-grey);
    white-space: nowrap;
    line-height: 1;
  }
  .brand-url {
    color: var(--text-grey);
    white-space: nowrap;
    line-height: 1;
  }
  .brand-url b { color: var(--lime-text); font-weight: 700; }

  /* Tall format header */
  .tall .brand-head { height: 162px; text-align: center; }
  .tall .brand-mark { width: 50px; height: 50px; margin: 16px auto 0; }
  .tall .brand-name { font-size: 18px; margin-top: 36px; }
  .tall .brand-url { font-size: 10.5px; margin-top: 6px; }
  .tall .brand-curve { top: 160px; height: 14px; }

  /* Box format header */
  .box .brand-head { height: 76px; }
  .box .brand-mark { position: absolute; left: 10px; top: 8px; width: 48px; height: 48px; }
  .box .brand-name { position: absolute; left: 66px; top: 14px; font-size: 26px; }
  .box .brand-url { position: absolute; left: 68px; top: 49px; font-size: 14px; }
  .box .brand-curve { top: 74px; height: 18px; }

  /* Wide format brand panel */
  .wide .brand-panel { position: absolute; left: 0; top: 0; width: 345px; height: 100%; }
  .wide .brand-panel svg { position: absolute; inset: 0; width: 100%; height: 100%; }
  .wide .brand-mark { position: absolute; left: 12px; top: 18px; width: 52px; height: 52px; }
  .wide .brand-name { position: absolute; left: 74px; top: 15px; font-size: 29px; }
  .wide .brand-url { position: absolute; left: 76px; top: 57px; font-size: 17px; }

  /* Messaging */
  .headline {
    position: absolute;
    background: var(--panel-dark);
    color: var(--text-white);
    font-family: "Arvo", Georgia, serif;
    font-weight: 700;
    line-height: 1.05;
    white-space: nowrap;
  }
  .headline em { font-style: normal; color: var(--lime-text); }
  .subline {
    position: absolute;
    background: var(--lime);
    color: var(--sub-dark);
    font-family: "Arvo", Georgia, serif;
    font-weight: 700;
    line-height: 1.25;
    white-space: nowrap;
  }
  .subline em { font-style: normal; color: var(--text-white); }
  .cta {
    position: absolute;
    border-radius: 4px;
    background: linear-gradient(var(--btn-top), var(--btn-bottom));
    color: var(--btn-text);
    font-family: "Arvo", Georgia, serif;
    font-weight: 700;
    text-align: center;
    box-shadow: 0 2px 3px rgba(0,0,0,.35);
    white-space: nowrap;
  }

  .tall .headline { left: 0; width: 100%; font-size: 19px; padding: 8px 0 7px; text-align: center; }
  .tall .subline { left: 0; width: 100%; font-size: 11.5px; padding: 5px 0 6px; text-align: center; }
  .tall .cta { left: 15px; width: 130px; height: 32px; line-height: 32px; font-size: 14px; }

  .box .headline { font-size: 19px; padding: 4px 0 4px 12px; }
  .box .subline { font-size: 11px; padding: 2px 0 2px 6px; }
  .box .cta { width: 130px; height: 31px; line-height: 31px; font-size: 14px; }

  .wide .headline { right: 0; font-size: 19px; padding: 4px 10px 4px 12px; }
  .wide .subline { right: 0; font-size: 11px; padding: 2px 6px; }
  .wide .cta { width: 131px; height: 31px; line-height: 31px; font-size: 14px; }
</style>
</head>
<body>

  <!-- Wide skyscraper, centred messaging -->
  <section class="banner tall" style="left:53px; top:65px; width:162px; height:602px;">
    <div class="map-fill" role="img" aria-label="Topographic map excerpt with orange contour lines, blue streams and grid"></div>
    <header class="brand-head">
      <span class="brand-mark"></span>
      <p class="brand-name">Kea Ridge Charts</p>
      <p class="brand-url">www.<b>kearidgecharts</b>.co.nz</p>
    </header>
    <svg class="brand-curve" viewBox="0 0 160 14" preserveAspectRatio="none" aria-hidden="true">
      <path d="M0 0H160V3Q80 14 0 3Z" fill="var(--panel-dark)"/>
      <path d="M0 5Q80 16 160 5" fill="none" stroke="var(--lime)" stroke-width="3"/>
    </svg>
    <p class="headline" style="top:268px;">FREE ONLINE<br><em>TOPO MAP</em></p>
    <p class="subline" style="top:332px;">USING THE OFFICIAL<br><em>VOMR TOPO MAPS</em></p>
    <a class="cta" style="top:555px;">EXPLORE NOW!</a>
  </section>

  <!-- Wide skyscraper, footer messaging -->
  <section class="banner tall" style="left:233px; top:65px; width:162px; height:602px;">
    <div class="map-fill" role="img" aria-label="Topographic map excerpt with orange contour lines, hill summit and streams"></div>
    <header class="brand-head">
      <span class="brand-mark"></span>
      <p class="brand-name">Kea Ridge Charts</p>
      <p class="brand-url">www.<b>kearidgecharts</b>.co.nz</p>
    </header>
    <svg class="brand-curve" viewBox="0 0 160 14" preserveAspectRatio="none" aria-hidden="true">
      <path d="M0 0H160V3Q80 14 0 3Z" fill="var(--panel-dark)"/>
      <path d="M0 5Q80 16 160 5" fill="none" stroke="var(--lime)" stroke-width="3"/>
    </svg>
    <p class="headline" style="top:500px;">FREE ONLINE<br><em>TOPO MAP</em></p>
    <p class="subline" style="top:560px; height:42px;">USING THE OFFICIAL<br><em>VOMR TOPO MAPS</em></p>
  </section>

  <!-- Medium rectangle with button -->
  <section class="banner box" style="left:413px; top:195px; width:302px; height:252px;">
    <div class="map-fill" role="img" aria-label="Topographic map excerpt with orange contours and blue streams"></div>
    <header class="brand-head">
      <span class="brand-mark"></span>
      <p class="brand-name">Kea Ridge Charts</p>
      <p class="brand-url">www.<b>kearidgecharts</b>.co.nz</p>
    </header>
    <svg class="brand-curve" viewBox="0 0 300 18" preserveAspectRatio="none" aria-hidden="true">
      <path d="M0 0H300V4Q150 20 0 4Z" fill="var(--panel-dark)"/>
      <path d="M0 6Q150 22 300 6" fill="none" stroke="var(--lime)" stroke-width="3"/>
    </svg>
    <p class="headline" style="left:0; top:123px; width:288px;">FREE ONLINE <em>TOPO MAP</em></p>
    <p class="subline" style="left:28px; top:153px; width:272px;">USING THE OFFICIAL <em>VOMR TOPO MAPS</em></p>
    <a class="cta" style="left:84px; top:212px;">EXPLORE NOW!</a>
  </section>

  <!-- Medium rectangle, footer messaging -->
  <section class="banner box" style="left:733px; top:195px; width:302px; height:252px;">
    <div class="map-fill" role="img" aria-label="Topographic map excerpt with orange contours and blue streams"></div>
    <header class="brand-head">
      <span class="brand-mark"></span>
      <p class="brand-name">Kea Ridge Charts</p>
      <p class="brand-url">www.<b>kearidgecharts</b>.co.nz</p>
    </header>
    <svg class="brand-curve" viewBox="0 0 300 18" preserveAspectRatio="none" aria-hidden="true">
      <path d="M0 0H300V4Q150 20 0 4Z" fill="var(--panel-dark)"/>
      <path d="M0 6Q150 22 300 6" fill="none" stroke="var(--lime)" stroke-width="3"/>
    </svg>
    <p class="headline" style="left:0; top:200px; width:300px;">FREE ONLINE <em>TOPO MAP</em></p>
    <p class="subline" style="left:28px; top:230px; width:272px;">USING THE OFFICIAL <em>VOMR TOPO MAPS</em></p>
  </section>

  <!-- Leaderboard with button -->
  <section class="banner wide" style="left:413px; top:465px; width:730px; height:92px;">
    <div class="map-fill" role="img" aria-label="Topographic map excerpt with road, orange contours and streams"></div>
    <div class="brand-panel">
      <svg viewBox="0 0 345 92" preserveAspectRatio="none" aria-hidden="true">
        <path d="M0 0H325Q345 46 325 92H0Z" fill="var(--panel-dark)"/>
        <path d="M327 0Q349 46 327 92" fill="none" stroke="var(--lime)" stroke-width="5"/>
      </svg>
      <span class="brand-mark"></span>
      <p class="brand-name">Kea Ridge Charts</p>
      <p class="brand-url">www.<b>kearidgecharts</b>.co.nz</p>
    </div>
    <p class="headline" style="top:1px; width:300px;">FREE ONLINE <em>TOPO MAP</em></p>
    <p class="subline" style="top:32px; width:272px;">USING THE OFFICIAL <em>VOMR TOPO MAPS</em></p>
    <a class="cta" style="left:592px; top:55px;">EXPLORE NOW!</a>
  </section>

  <!-- Leaderboard, messaging only -->
  <section class="banner wide" style="left:413px; top:575px; width:730px; height:92px;">
    <div class="map-fill coastal" role="img" aria-label="Topographic map excerpt with coastline, bay, road and orange contours"></div>
    <div class="brand-panel">
      <svg viewBox="0 0 345 92" preserveAspectRatio="none" aria-hidden="true">
        <path d="M0 0H325Q345 46 325 92H0Z" fill="var(--panel-dark)"/>
        <path d="M327 0Q349 46 327 92" fill="none" stroke="var(--lime)" stroke-width="5"/>
      </svg>
      <span class="brand-mark"></span>
      <p class="brand-name">Kea Ridge Charts</p>
      <p class="brand-url">www.<b>kearidgecharts</b>.co.nz</p>
    </div>
    <p class="headline" style="top:40px; width:300px;">FREE ONLINE <em>TOPO MAP</em></p>
    <p class="subline" style="top:71px; width:272px;">USING THE OFFICIAL <em>VOMR TOPO MAPS</em></p>
  </section>

</body>
</html>
```